Brisk Tutorium Website

We are looking for a new design of our website. The current website is www.brisktutorium.example. The company is the #1 pre-college math and science program in Orange County, CA. We would like to see designs that integrate our logo with a modern color scheme. We are also open for suggestions that could improve our logo. We would like a simple, minimal, clean, classy, and vibrant front-page user interface design that give the premium, modern, innovative, creative, and premier brand feel. We like the "New Retro Colors for the Web" as described here: http://www.pixel-layoutnook.example/en/layout-notes-2013/.

Target Market(s)

The target market is parents with K-12 students from a diverse population. Parents are well educated with family income > $150,000. Most of the decision makers are mothers from immigrate families: 30% Chinese, 30% Korean, 15% Indian, 24% White.

Industry/Entity Type

College

Requirements
Must have
• Must read our statement of differentiation at:
• http://brisktutorium.example/about-us
• Your design must be reflective of your understanding of the statements.
Nice to have
• The design should also be mobil friendly.
Should not have
• While most of our current classes are math, our company is expanding to include STEM (Science, Technology, Engineering, and Math) for gifted students. Therefore, the site should not be JUST a math education site.

```html
<!DOCTYPE html>
<html lang="en">
<head>
<meta charset="utf-8">
<title>Brisk Tutorium – Home</title>
<link rel="stylesheet" href="https://fonts.googleapis.com/css2?family=Open+Sans:wght@400;600;700&family=Noto+Sans:wght@400;700&display=swap">
<style>
  :root {
    --navy: #1f2a7a;
    --navy-text: #1c2777;
    --slate: #353b48;
    --green: #4fab47;
    --menu-muted: #aab1d0;
    --ink: #222222;
    --body-ink: #333333;
    --rule: #7c9a6c;
    --tile-orange: #f05a28;
    --tile-blue: #1a4f9c;
    --tile-green: #1e8f3e;
    --tile-yellow: #f7b233;
    --bullet: #8a93a6;
    --white: #ffffff;
  }
  html, body { margin: 0; padding: 0; overflow: hidden; background: var(--white); }
  .canvas { position: relative; width: 1200px; height: 533px; overflow: hidden; background: var(--white); }
  .stage { position: absolute; left: 0; top: 0; width: 963px; height: 428px; transform: scale(1.2461); transform-origin: 0 0; font-family: "Open Sans", sans-serif; }

  .brand { position: absolute; left: 20px; top: 12px; display: flex; align-items: center; gap: 14px; }
  .brand-dot { width: 54px; height: 54px; border-radius: 50%; background: var(--navy); }
  .brand-name { font-family: "Open Sans", sans-serif; font-weight: 700; font-size: 25px; color: var(--navy-text); letter-spacing: 0.3px; }

  .top-nav { position: absolute; left: 320px; top: 22px; width: 628px; height: 50px; background: var(--navy); border-radius: 4px; }
  .top-nav-item { position: absolute; left: 20px; top: 13px; color: var(--white); font-size: 16px; }
  .top-nav-pointer { position: absolute; left: 383px; top: 71px; width: 0; height: 0; border-left: 7px solid transparent; border-right: 7px solid transparent; border-top: 8px solid var(--navy); }

  .dropdown { position: absolute; left: 223px; top: 84px; width: 234px; height: 104px; background: var(--navy); border-radius: 4px; z-index: 5; padding-top: 2px; box-sizing: border-box; }
  .dropdown-item { height: 32px; margin: 0 4px 2px; padding-left: 7px; line-height: 32px; color: var(--white); font-size: 13px; border-radius: 2px; }
  .dropdown-item.is-selected { background: var(--green); }

  .side-menu { position: absolute; left: 13px; top: 93px; width: 280px; }
  .side-menu-title { height: 52px; background: var(--slate); color: var(--white); font-weight: 600; font-size: 21px; line-height: 50px; padding-left: 66px; }
  .side-menu-item { height: 50px; border-top: 1px solid var(--white); background: var(--navy); color: var(--menu-muted); font-size: 16px; line-height: 50px; padding-left: 55px; }
  .side-menu-item.is-selected { border-top: none; height: 51px; background: var(--green); color: var(--white); padding-left: 30px; display: flex; align-items: center; gap: 8px; }

  .content { position: absolute; left: 322px; top: 98px; width: 626px; font-family: "Noto Sans", Verdana, sans-serif; }
  .content-title { margin: 0; font-size: 15.5px; font-weight: 700; color: var(--ink); letter-spacing: 1.1px; padding-left: 4px; white-space: nowrap; }
  .content-tools { position: absolute; right: 2px; top: 8px; display: flex; gap: 4px; }
  .content-rule { height: 1px; background: var(--rule); margin: 1px 0 0 138px; width: 470px; }
  .content-intro { margin: 5px 0 0; font-size: 10.6px; font-weight: 700; line-height: 14.4px; color: var(--ink); padding-left: 4px; letter-spacing: 0.35px; }

  .tiles { position: absolute; left: 322px; top: 200px; display: flex; gap: 5px; }
  .tile { width: 125px; height: 90px; position: relative; }
  .tile-art { position: absolute; left: 4px; top: 4px; right: 4px; height: 52px; background: linear-gradient(180deg, #ffffff, #e6ebe4); }
  .tile-label { position: absolute; left: 0; right: 0; bottom: 10px; text-align: center; color: var(--white); font-family: "Noto Sans", Verdana, sans-serif; font-weight: 700; font-size: 14px; }
  .tile-elearning { background: var(--tile-orange); }
  .tile-scheduler { background: var(--tile-blue); }
  .tile-newsletter { background: var(--tile-green); }
  .tile-registration { background: var(--tile-yellow); }

  .link-notes { position: absolute; left: 326px; top: 300px; width: 620px; margin: 0; padding: 0; list-style: none; font-family: "Noto Sans", Verdana, sans-serif; font-size: 10.8px; line-height: 14px; color: var(--body-ink); }
  .link-notes li { position: relative; padding-left: 12px; margin-bottom: 4px; }
  .link-notes li::before { content: ""; position: absolute; left: 0; top: 5px; width: 5px; height: 5px; background: var(--bullet); }
</style>
</head>
<body>
<div class="canvas">
  <div class="stage">
    <header class="brand">
      <span class="brand-dot"></span>
      <span class="brand-name">BRISK TUTORIUM</span>
    </header>

    <nav class="top-nav">
      <span class="top-nav-item">Menu Item</span>
    </nav>
    <span class="top-nav-pointer"></span>

    <ul class="dropdown" style="list-style:none;margin:0;">
      <li class="dropdown-item">Element One</li>
      <li class="dropdown-item is-selected">Element Selected</li>
      <li class="dropdown-item">Element Three</li>
    </ul>

    <aside class="side-menu">
      <div class="side-menu-title">Vertical Menu</div>
      <div class="side-menu-item is-selected">
        <svg width="16" height="14" viewBox="0 0 16 14" aria-hidden="true">
          <path d="M1 7 L3.5 1 H12.5 L15 7 V13 H1 Z" fill="none" stroke="#fff" stroke-width="1.6"/>
          <path d="M1 7 H5 L6 9 H10 L11 7 H15" fill="none" stroke="#fff" stroke-width="1.6"/>
        </svg>
        <span>Selected element</span>
      </div>
      <div class="side-menu-item">Menu element</div>
      <div class="side-menu-item">Menu element</div>
      <div class="side-menu-item">Menu element</div>
      <div class="side-menu-item">Menu element</div>
    </aside>

    <main class="content">
      <h1 class="content-title">Gifted Math and Problem Solving Training Programs</h1>
      <div class="content-tools">
        <svg width="14" height="10" viewBox="0 0 14 10" aria-hidden="true"><rect x="0.5" y="0.5" width="13" height="9" fill="#dfe6f0" stroke="#6a7a94"/><path d="M0.5 0.5 L7 5.5 L13.5 0.5" fill="none" stroke="#6a7a94"/></svg>
        <svg width="14" height="12" viewBox="0 0 14 12" aria-hidden="true"><rect x="3" y="0.5" width="8" height="4" fill="#fff" stroke="#666"/><rect x="0.5" y="4" width="13" height="5" fill="#bbb" stroke="#666"/><rect x="3" y="7" width="8" height="4.5" fill="#fff" stroke="#666"/></svg>
      </div>
      <div class="content-rule"></div>
      <p class="content-intro">Welcome to Brisk Tutorium Academy for Gifted Youth. We provide after-school enrichment programs in math, physics, chemistry, biology, and computer science, mentor middle and high school students on science projects, and offer college counseling to aspiring students in pursuing top ranked colleges. Please explore this website to learn more about our programs and the path to an inspired education.</p>
    </main>

    <section class="tiles">
      <div class="tile tile-elearning"><div class="tile-art" role="img" aria-label="Illustration of an open notebook with a pen"></div><span class="tile-label">eLearning</span></div>
      <div class="tile tile-scheduler"><div class="tile-art" role="img" aria-label="Illustration of a clock over a calendar grid"></div><span class="tile-label">Scheduler</span></div>
      <div class="tile tile-newsletter"><div class="tile-art" role="img" aria-label="Illustration of a printed newsletter page"></div><span class="tile-label">Newsletter</span></div>
      <div class="tile tile-registration"><div class="tile-art" role="img" aria-label="Illustration of a check box with a tick mark"></div><span class="tile-label">Registration</span></div>
    </section>

    <ul class="link-notes">
      <li>Click on eLearning to access our Online Learning Management System for current students and families.</li>
      <li>Click on Scheduler to make an appointment online for qualifying exams, gathering information, college counseling, or science research meetings.</li>
      <li>Click on Newsletter to subscribe to our monthly newsletter - The Brisk Learner.</li>
      <li>Click on Registration to sign up for our classes.</li>
    </ul>
  </div>
</div>
</body>
</html>
```